Simple, Professional and neat business card design for Vendralo Inc.

We're looking to re-vamp our business card design. We're a supplier of innovative feed ingredients for the North American animal agriculture industry. We are located in Lucknow, Ontario, Canada and our flagship product is a product that prevents milk fever in dairy cows when the calve, it is fed before calving and is very effective compared to other alternatives available on the market today.

Our company has Danish roots and we import all of our product from our Danish partner/manufacturer in Denmark. We like our design to embrace high professionalism while remaining neat and simple.

Target Market(s)

B2B, Feed Mills, Veterinary Clinics, Large integrators/producers,

Industry/Entity Type

Agribusiness

Contact Information for Business Card

We like the rounded corners because they make the card easy to sit in a wallet and not many use it so it makes the card stand out, just possibly something to take account for during the design.

As you can also see on the sliders below, looking for a that simple but proffesional scandinavian design.

Requirements
Nice to have
• Rounded corners
Should not have
• Too vibrant

```html
<!DOCTYPE html>
<html lang="en">
<head>
<meta charset="utf-8">
<title>Vendralo Inc. — Business Card</title>
<link rel="stylesheet" href="https://fonts.googleapis.com/css2?family=Lato:wght@700;900&family=Open+Sans:ital,wght@0,400;0,600;0,700;1,600&display=swap">
<style>
  :root {
    --backdrop: #26282c;
    --navy: #0c3f86;
    --blue: #1a5bb0;
    --blue-light: #2f78cf;
    --gold: #e3c995;
    --gold-deep: #cfae6c;
    --paper: #ffffff;
    --paper-shade: #eef0f3;
    --ink: #3a3d42;
    --label: #1a5bb0;
  }
  * { box-sizing: border-box; margin: 0; padding: 0; }
  html, body {
    width: 1200px; height: 900px; overflow: hidden;
    background: var(--backdrop);
    font-family: "Open Sans", Arial, sans-serif;
  }
  .canvas { position: relative; width: 1200px; height: 900px; }

  .card {
    position: absolute;
    width: 520px; height: 300px;
    border-radius: 26px;
    overflow: hidden;
    box-shadow: 0 18px 40px rgba(0,0,0,.45);
  }

  /* ---------- Contact side ---------- */
  .card--contact {
    left: 60px; top: 440px;
    background: linear-gradient(135deg, var(--paper) 35%, var(--paper-shade) 100%);
    color: var(--ink);
  }
  .name-band {
    position: absolute; left: 0; top: 36px;
    width: 300px; height: 56px;
    background: linear-gradient(90deg, var(--navy), var(--blue));
    padding: 6px 0 0 34px;
    color: var(--paper);
  }
  .name-band__name { font-size: 22px; font-weight: 600; line-height: 1.15; }
  .name-band__title { font-size: 12px; font-style: italic; font-weight: 600; opacity: .9; }
  .band-mark {
    position: absolute; left: 300px; top: 36px; height: 56px;
    display: flex; align-items: center; gap: 8px; padding-left: 10px;
    font-size: 14px; font-weight: 700; color: var(--blue);
  }
  .band-mark__dot { width: 20px; height: 20px; border-radius: 50%; background: var(--gold); }

  .phones { position: absolute; left: 34px; top: 116px; font-size: 13.5px; line-height: 1.5; }
  .phones__label { color: var(--label); font-weight: 700; font-style: italic; }

  .details {
    position: absolute; right: 34px; bottom: 34px;
    text-align: right; font-size: 14px; line-height: 1.5;
  }
  .details__company { color: var(--label); font-weight: 700; font-size: 15px; }

  .bottom-strip {
    position: absolute; left: 0; right: 0; bottom: 0; height: 14px;
    background: linear-gradient(90deg, var(--navy), var(--blue));
  }

  /* ---------- Brand side ---------- */
  .card--brand { left: 620px; top: 150px; background: var(--gold); }
  .card--brand svg.face { position: absolute; inset: 0; }
  .brand-lockup {
    position: absolute; left: 0; right: 0; top: 92px;
    display: flex; align-items: center; justify-content: center; gap: 14px;
  }
  .brand-lockup__dot { width: 46px; height: 46px; border-radius: 50%; background: var(--gold); }
  .brand-lockup__name {
    font-family: "Lato", Arial, sans-serif; font-weight: 900;
    font-size: 34px; letter-spacing: .5px; color: var(--paper);
  }
  .social { position: absolute; left: 0; right: 0; top: 186px; display: flex; justify-content: center; gap: 16px; }
  .social__dot { width: 26px; height: 26px; border-radius: 50%; background: var(--gold); }
</style>
</head>
<body>
<main class="canvas">

  <section class="card card--brand" aria-label="Brand side of card">
    <svg class="face" width="520" height="300" viewBox="0 0 520 300" aria-hidden="true">
      <defs>
        <linearGradient id="brandBlue" x1="0" y1="0" x2="1" y2="1">
          <stop offset="0" style="stop-color: var(--navy)"/>
          <stop offset=".55" style="stop-color: var(--blue-light)"/>
          <stop offset="1" style="stop-color: var(--navy)"/>
        </linearGradient>
      </defs>
      <path d="M36 0 H520 V272 H372 Q352 272 346 286 L340 300 H0 V112 Q0 96 14 90 L24 86 Q36 80 36 66 Z" fill="url(#brandBlue)"/>
    </svg>
    <div class="brand-lockup">
      <span class="brand-lockup__dot"></span>
      <span class="brand-lockup__name">VENDRALO INC.</span>
    </div>
    <div class="social">
      <span class="social__dot"></span>
      <span class="social__dot"></span>
    </div>
  </section>

  <section class="card card--contact" aria-label="Contact side of card">
    <div class="name-band">
      <p class="name-band__name">Mikkel Rasmussen</p>
      <p class="name-band__title">Director</p>
    </div>
    <div class="band-mark"><span class="band-mark__dot"></span>Vendralo Inc.</div>

    <div class="phones">
      <p><span class="phones__label">M:</span> 555 214 0387</p>
      <p><span class="phones__label">O:</span> 555 326 4710</p>
      <p><span class="phones__label">Toll Free:</span> 800 555 0192</p>
      <p><span class="phones__label">Fax:</span> 555 326 4799</p>
    </div>

    <div class="details">
      <p>mikkel@vendralo.com</p>
      <p>www.vendralo.com</p>
      <p class="details__company">Vendralo INC.</p>
      <p>Box 42, Ardmore Ontario, Canada</p>
    </div>

    <div class="bottom-strip"></div>
  </section>

</main>
</body>
</html>
```